Cocktail-Making Assistant App re-design

Ok boys and girls, here's the deal:
I have an android app which is almost complete, but needs a design overhaul.

The app is a standard cocktail-making assistant: gives you a list of cocktails and the ability to see which cocktail you can make out of those ingredients (drinks, fruit, etc) you have at home.

I've attached some general app flow, as well as detailed requirements/explanation presentation. Most of those things are just FYI, so that you know what it's about.

3 screens are the most important (main screen, cocktail view screen, ingredient view screen), meaning I will pick the design mostly based on ideas for those 3 things, with the fourth being a rather simple list (given on attached flow, third tier)
Some other screens are derived from that, with some minor changes on it, but you shouldn't care about that.

There are lots of other, non-explained things which I said nothing about only because they are (from design point of view) completely the same and would only make it seem more complicated.

I don't want to influence the colour scheme, but the app will be released under RedCedar developer name (having a light colured red cedar as a logo) so I suppose some brownish design, for example, will not really fit nicely. If you, however, have a killer which you are confident will prove me wrong, I'm looking forward to seeing it!

It should be a serious, elegant look (as opposed to cartoonish, but we are not aiming for a business look at all!), not cluttered with details, no clubbing themes, glitter and so on.

Test apk file available on request (Android 2.3+).

Edit: payment is now guaranteed
Also please note that currently, the favorite, "heart" button has a motion effect:
on click it flies out of the screen to the left (white heart) and comes back to the screen as a red heart. Take that into consideration, if it means anything to you.

Reason: Some designers are enthusiastic but will need an extra weekend to polish their ideas.

Target Market(s)

Whoever you imagine would enjoy drinking cocktails

Industry/Entity Type

Business

Requirements
Must have
• Everything is said in the provided documentation - images say more than I could possibly write here.
Nice to have
• As said, most of the icons are a nice-to-have. Only those which are critically linked to the rest of the design must be provided. More details in the docs.
Should not have
• No cartoon look, No zillion colours

```html
<!DOCTYPE html>
<html lang="en">
<head>
<meta charset="utf-8">
<title>Cocktail Search – app screens</title>
<link href="https://fonts.googleapis.com/css2?family=Quicksand:wght@400;500&display=swap" rel="stylesheet">
<style>
:root{
  --stage:#d3d4d6;
  --screen:#ffffff;
  --screen-fade:#eeeeee;
  --bar:#29a9e1;
  --ink:#222222;
  --muted:#777777;
  --line:#e2e2e2;
  --field:#9a9a9a;
  --sky:#7ecdee;
  --lime:#a4f466;
  --berry:#cd6c95;
  --peach:#f7a872;
  --thumb:#a8dde2;
  --star:#b3b3b3;
}
*{box-sizing:border-box;margin:0;padding:0}
html,body{width:1200px;height:667px;overflow:hidden;background:var(--stage)}
body{position:relative;font-family:"Quicksand",sans-serif;color:var(--ink)}
h1,h2{font-weight:400}
.screen{position:absolute;width:364px;height:644px;background:linear-gradient(#fff 0,#fff 72%,var(--screen-fade) 100%)}
.screen--home{left:14px;top:6px}
.screen--hint{left:413px;top:8px}
.screen--list{left:817px;top:8px}
.app-bar{position:absolute;left:0;top:0;width:100%;height:62px;background:var(--bar);color:#fff}
.app-bar__title{position:absolute;left:0;right:0;top:15px;text-align:center;font-size:23px;font-weight:400}
.app-bar__icon{position:absolute;top:11px;width:40px;height:40px}
.app-bar__icon--home{left:10px}
.app-bar__icon--settings{right:8px}
.search-label{position:absolute;left:26px;top:76px;font-size:21px;font-weight:400}
.search-field{position:absolute;left:41px;top:113px;width:290px;height:33px;border:2px solid var(--field);background:#fff;font-size:12.5px;color:#555;padding:6px 11px}
.search-field svg{position:absolute;right:7px;top:4px}
.hint{position:absolute;left:70px;right:70px;top:169px;text-align:center;font-size:11px;line-height:16.5px;color:var(--muted)}
.category-list,.drink-list{position:absolute;left:3px;right:3px;list-style:none;border-top:3px solid var(--line)}
.category-list--home{top:231px}
.category-list--hint{top:271px}
.category{position:relative;height:70px;border-bottom:3px solid var(--line);background:linear-gradient(#fff,#f7f7f7)}
.category__swatch{position:absolute;left:2px;top:5px;width:21px;height:56px}
.category__name{position:absolute;left:73px;top:16px;font-size:18px}
.category__note{position:absolute;left:73px;top:40px;font-size:8.5px;color:var(--muted)}
.swatch--sky{background:var(--sky)}.swatch--lime{background:var(--lime)}.swatch--berry{background:var(--berry)}.swatch--peach{background:var(--peach)}
.crumb{position:absolute;left:6px;top:178px}
.crumb__title{position:absolute;left:142px;top:189px;font-size:18px}
.crumb__note{position:absolute;left:142px;top:210px;font-size:8.5px;color:var(--muted)}
.drink-list{top:266px}
.drink{position:relative;height:70px;border-bottom:3px solid var(--line);background:linear-gradient(#fff,#f7f7f7)}
.drink__thumb{position:absolute;left:4px;top:5px;width:57px;height:57px;border-radius:50%;background:var(--thumb)}
.drink__name{position:absolute;left:72px;top:16px;font-size:18px}
.drink__rating{position:absolute;left:71px;top:42px}
.drink__stock{position:absolute;right:9px;top:51px;font-size:10px;color:var(--muted)}
</style>
</head>
<body>
<svg width="0" height="0" style="position:absolute">
  <defs>
    <symbol id="icon-home" viewBox="0 0 40 40"><circle cx="20" cy="20" r="17" fill="none" stroke="#fff" stroke-width="3"/><path d="M11 20 20 12 29 20H26V28H22V23H18V28H14V20Z" fill="#fff"/></symbol>
    <symbol id="icon-gear" viewBox="0 0 40 40"><circle cx="20" cy="20" r="17" fill="none" stroke="#fff" stroke-width="3"/><g fill="#fff"><circle cx="20" cy="20" r="8"/><rect x="17.5" y="8" width="5" height="24" rx="1"/><rect x="8" y="17.5" width="24" height="5" rx="1"/><rect x="17.5" y="8" width="5" height="24" rx="1" transform="rotate(45 20 20)"/><rect x="17.5" y="8" width="5" height="24" rx="1" transform="rotate(-45 20 20)"/></g><circle cx="20" cy="20" r="3.5" fill="var(--bar)"/></symbol>
    <symbol id="icon-search" viewBox="0 0 24 24"><circle cx="10" cy="10" r="7" fill="none" stroke="#ddd" stroke-width="2.5"/><path d="M15 15 22 22" stroke="#ddd" stroke-width="3.5" stroke-linecap="round"/></symbol>
    <symbol id="star-full" viewBox="0 0 20 20"><path d="M10 1.5 12.6 7.2 18.8 7.8 14.1 11.9 15.5 18 10 14.8 4.5 18 5.9 11.9 1.2 7.8 7.4 7.2Z" fill="var(--star)"/></symbol>
    <symbol id="star-empty" viewBox="0 0 20 20"><path d="M10 1.5 12.6 7.2 18.8 7.8 14.1 11.9 15.5 18 10 14.8 4.5 18 5.9 11.9 1.2 7.8 7.4 7.2Z" fill="none" stroke="var(--star)" stroke-width="1.3"/></symbol>
  </defs>
</svg>

<section class="screen screen--home">
  <header class="app-bar"><svg class="app-bar__icon app-bar__icon--home"><use href="#icon-home"/></svg><h1 class="app-bar__title">Cocktail Search</h1><svg class="app-bar__icon app-bar__icon--settings"><use href="#icon-gear"/></svg></header>
  <h2 class="search-label">Search</h2>
  <div class="search-field">Tap here to edit text . . .<svg width="24" height="24"><use href="#icon-search"/></svg></div>
  <ul class="category-list category-list--home">
    <li class="category"><span class="category__swatch swatch--sky"></span><span class="category__name">All Drinks</span><span class="category__note">Including cocktails, party drinks, and much more</span></li>
    <li class="category"><span class="category__swatch swatch--lime"></span><span class="category__name">Party Drinks</span><span class="category__note">Lorem Ipsum dolor , sit, amet</span></li>
    <li class="category"><span class="category__swatch swatch--berry"></span><span class="category__name">Lorem ipsum</span><span class="category__note">Including cocktails, party drinks, and much more</span></li>
    <li class="category"><span class="category__swatch swatch--peach"></span><span class="category__name">Cocktails</span><span class="category__note">sample , text , placed, here</span></li>
  </ul>
</section>

<section class="screen screen--hint">
  <header class="app-bar"><svg class="app-bar__icon app-bar__icon--home"><use href="#icon-home"/></svg><h1 class="app-bar__title">Cocktail Search</h1><svg class="app-bar__icon app-bar__icon--settings"><use href="#icon-gear"/></svg></header>
  <h2 class="search-label">Search</h2>
  <div class="search-field">Tap here to edit text . . .<svg width="24" height="24"><use href="#icon-search"/></svg></div>
  <p class="hint">You can search the entire collection of all categories or else simply select a subcategory from below list.</p>
  <ul class="category-list category-list--hint">
    <li class="category"><span class="category__swatch swatch--sky"></span><span class="category__name">All Drinks</span><span class="category__note">Including cocktails, party drinks, and much more</span></li>
    <li class="category"><span class="category__swatch swatch--lime"></span><span class="category__name">Party Drinks</span><span class="category__note">Lorem Ipsum dolor , sit, amet</span></li>
    <li class="category"><span class="category__swatch swatch--berry"></span><span class="category__name">Lorem ipsum</span><span class="category__note">Including cocktails, party drinks, and much more</span></li>
    <li class="category"><span class="category__swatch swatch--peach"></span><span class="category__name">Cocktails</span><span class="category__note">sample , text , placed, here</span></li>
  </ul>
</section>

<section class="screen screen--list">
  <header class="app-bar"><svg class="app-bar__icon app-bar__icon--home"><use href="#icon-home"/></svg><h1 class="app-bar__title">Cocktail Search</h1><svg class="app-bar__icon app-bar__icon--settings"><use href="#icon-gear"/></svg></header>
  <h2 class="search-label">Search</h2>
  <div class="search-field">Tap here to edit text . . .<svg width="24" height="24"><use href="#icon-search"/></svg></div>
  <svg class="crumb" width="124" height="58" viewBox="0 0 124 58">
    <path d="M80 0H104L124 29 104 58H80L100 29Z" fill="var(--lime)"/>
    <path d="M0 0H80L100 29 80 58H0Z" fill="var(--bar)"/>
    <circle cx="23" cy="28" r="17" fill="none" stroke="#fff" stroke-width="3"/>
    <path d="M32 28H16M22 21 15 28 22 35" fill="none" stroke="#fff" stroke-width="3" stroke-linecap="round" stroke-linejoin="round"/>
  </svg>
  <span class="crumb__title">Party Drinks</span>
  <span class="crumb__note">Lorem Ipsum dolor , sit, amet</span>
  <ul class="drink-list">
    <li class="drink"><span class="drink__thumb" role="img" aria-label="57 Lagoon drink photo"></span><span class="drink__name">57 Lagoon</span>
      <svg class="drink__rating" width="100" height="18"><use href="#star-full" x="0" width="18" height="18"/><use href="#star-full" x="20" width="18" height="18"/><use href="#star-full" x="40" width="18" height="18"/><use href="#star-empty" x="60" width="18" height="18"/><use href="#star-empty" x="80" width="18" height="18"/></svg><span class="drink__stock">Have &nbsp;2 out of 4</span></li>
    <li class="drink"><span class="drink__thumb" role="img" aria-label="57 Lagoon No.2 drink photo"></span><span class="drink__name">57 Lagoon No.2</span>
      <svg class="drink__rating" width="100" height="18"><use href="#star-full" x="0" width="18" height="18"/><use href="#star-full" x="20" width="18" height="18"/><use href="#star-full" x="40" width="18" height="18"/><use href="#star-empty" x="60" width="18" height="18"/><use href="#star-empty" x="80" width="18" height="18"/></svg><span class="drink__stock">Have &nbsp;0 out of 4</span></li>
    <li class="drink"><span class="drink__thumb" role="img" aria-label="110 in the shade drink photo"></span><span class="drink__name">110 in the shade</span>
      <svg class="drink__rating" width="100" height="18"><use href="#star-full" x="0" width="18" height="18"/><use href="#star-empty" x="20" width="18" height="18"/><use href="#star-empty" x="40" width="18" height="18"/><use href="#star-empty" x="60" width="18" height="18"/><use href="#star-empty" x="80" width="18" height="18"/></svg><span class="drink__stock">Have &nbsp;2 out of 7</span></li>
    <li class="drink"><span class="drink__thumb" role="img" aria-label="155 Belmont drink photo"></span><span class="drink__name">155 Belmont</span>
      <svg class="drink__rating" width="100" height="18"><use href="#star-empty" x="0" width="18" height="18"/><use href="#star-empty" x="20" width="18" height="18"/><use href="#star-empty" x="40" width="18" height="18"/><use href="#star-empty" x="60" width="18" height="18"/><use href="#star-empty" x="80" width="18" height="18"/></svg><span class="drink__stock">Have &nbsp;1 out of 9</span></li>
  </ul>
</section>
</body>
</html>
```